Parcelnook.com.au Front page Re-Design

We need a front page redesign for the website parcelnook.com.au,
The site needs to keep a number of products products highlighted on the front page. Same buttons but navigation could be different and we still need some text for SEO.
What we do not currently like:
1. The big banners.
2. The use of too much orange especially the 50% orange borders.
3. the fact that products cannot be seen straight away when logged-in.
4. The fact that it is hard to convert to tablet friendly
5. The fact that it's not a modern design.

What we think we want:

1. Maybe more use of 1 colour (purple or orange) with the other a secondary highlight colour.
2. A more modern look
3. The wow factor

Look at parcelnook.com.au take the elements that you need and design.
Updates

Reason: Designs are getting better. liking the designs that don't look like the usual e-commerce templates out there.

Hello,

We are making decisions next Monday. Sorry for the delay but there has been a lot of holidays in Australia and decision makers away.

Industry/Entity Type

Seo

Colors
6b449b
f78f20
ffffff

```html
<!DOCTYPE html>
<html lang="en">
<head>
<meta charset="utf-8">
<title>Parcelnook.com.au – Gift Baskets & Hampers</title>
<link href="https://fonts.googleapis.com/css2?family=Open+Sans:wght@400;600;700&display=swap" rel="stylesheet">
<style>
:root{
  --purple:#6b449b;
  --purple-deep:#4f2f78;
  --purple-soft:#efe8f6;
  --orange:#f78f20;
  --ink:#333333;
  --muted:#666666;
  --line:#e2dcea;
  --page:#f7f5fa;
  --white:#ffffff;
  --footer:#3b2a52;
  --footer-text:#ece6f4;
  --footer-link:#c8b9dc;
  --shadow:0 2px 8px rgba(60,30,100,.08);
}
*{box-sizing:border-box;margin:0;padding:0}
html,body{width:836px;height:1200px;overflow:hidden}
body{font-family:"Open Sans",Arial,sans-serif;color:var(--ink);background:var(--page);position:relative;font-size:10px}
a{color:inherit;text-decoration:none}

.utility-bar{position:absolute;left:0;top:0;width:836px;height:22px;background:var(--purple-deep);color:var(--white);font-size:10px}
.utility-bar .util{position:absolute;top:4px;display:flex;align-items:center;gap:5px}
.utility-bar svg{width:10px;height:10px;fill:var(--white)}
.search-box{position:absolute;left:682px;top:4px;width:100px;height:14px;background:var(--white);border-radius:7px}
.search-box svg{position:absolute;right:5px;top:2px;width:10px;height:10px;fill:none;stroke:#999;stroke-width:1.6}

.site-header{position:absolute;left:0;top:22px;width:836px;height:74px;background:var(--white)}
.brand{position:absolute;left:43px;top:22px;display:flex;align-items:center;gap:8px}
.brand-square{width:30px;height:30px;background:var(--orange);border-radius:6px}
.brand-name{font-size:22px;font-weight:700;color:var(--purple);letter-spacing:-.3px}
.perk{position:absolute;top:26px;display:flex;align-items:center;gap:6px}
.perk svg{width:20px;height:20px;fill:none;stroke:var(--purple);stroke-width:1.8}
.perk strong{display:block;color:var(--purple);font-size:10.5px;font-weight:700;line-height:12px}
.perk small{display:block;font-size:7px;color:var(--muted);line-height:9px}
.social{position:absolute;left:652px;top:28px;display:flex;gap:6px}
.social span{width:21px;height:21px;border-radius:50%;background:var(--purple)}

.main-nav{position:absolute;left:0;top:96px;width:836px;height:24px;background:var(--white);border-top:1px solid var(--line);border-bottom:1px solid var(--line)}
.main-nav ul{list-style:none;display:flex;gap:15px;position:absolute;left:43px;top:4px;font-size:10px;color:#222}
.main-nav li.current{color:var(--orange);font-weight:600}

.promo-banner{position:absolute;left:42px;top:137px;width:742px;height:52px;background:var(--white);border-left:4px solid var(--orange);border-radius:6px;box-shadow:var(--shadow);color:var(--ink);text-align:center}
.promo-banner h2{font-size:17px;font-weight:400;margin-top:6px;line-height:20px;color:var(--purple)}
.promo-banner h2 b{font-weight:700}
.promo-banner p{font-size:12px;line-height:16px;color:var(--muted)}
.promo-banner p b{color:var(--orange)}

.sidebar{position:absolute;left:42px;top:208px;width:174px}
.side-block{margin-bottom:22px}
.side-block h3{font-size:13px;font-weight:400;color:var(--purple);padding-bottom:4px;border-bottom:1px solid var(--line);position:relative}
.side-block h3::after{content:"";position:absolute;left:0;bottom:-1px;width:125px;height:2px;background:var(--purple)}
.side-block h3 .chev{position:absolute;right:6px;top:6px;width:7px;height:5px}
.side-block ul{list-style:none;margin-top:12px;padding-left:14px}
.side-block li{font-size:9.5px;color:#555;height:21.6px;position:relative}
.side-block li::after{content:"";position:absolute;right:14px;top:4px;width:4px;height:4px;border-right:1px solid #a99bbd;border-top:1px solid #a99bbd;transform:rotate(45deg)}
.chev{fill:none;stroke:#a99bbd;stroke-width:1.2}

.category{position:absolute;top:215px;width:173px;height:248px;background:var(--white);border-radius:8px;overflow:hidden;box-shadow:var(--shadow)}
.category .photo{height:204px}
.category .label{position:absolute;left:0;bottom:0;width:100%;height:44px;background:var(--c);color:var(--white);text-align:center}
.category .label b{display:block;font-size:17px;font-weight:400;margin-top:5px;line-height:20px}
.category .label span{font-size:9px}

.section-title{position:absolute;font-size:13px;font-weight:400;color:var(--purple);border-bottom:1px solid var(--line);padding-bottom:3px}
.slider-arrows{position:absolute;right:0;top:2px;display:flex;gap:3px}
.slider-arrows span{width:13px;height:13px;border:1px solid var(--purple);border-radius:50%;display:flex;align-items:center;justify-content:center}
.slider-arrows svg{width:5px;height:7px;fill:var(--purple)}

.products{position:absolute;left:232px;top:530px;width:361px;display:grid;grid-template-columns:repeat(3,116px);gap:9px 6.5px}
.product{height:182px;background:var(--white);border:1px solid var(--line);border-radius:6px;text-align:center;position:relative;box-shadow:var(--shadow);overflow:hidden}
.product.featured{border-color:var(--purple)}
.product .photo{height:112px;margin:4px;border-radius:4px}
.product h4{font-size:7.5px;font-weight:700;color:#333;line-height:9px;height:20px;padding:0 6px;display:flex;align-items:center;justify-content:center}
.product.featured h4{color:var(--purple)}
.product .price{font-size:13px;margin-top:3px;color:var(--ink)}
.product .actions{position:absolute;left:4px;right:4px;bottom:4px;display:flex;justify-content:space-between;font-size:6.5px;color:#444}
.product .actions span{display:flex;align-items:center;gap:2px}
.product .actions i{width:7px;height:7px;border-radius:50%;background:var(--purple);color:var(--white);font-style:normal;font-size:7px;line-height:7px}

.aside{position:absolute;left:611px;top:497px;width:173px}
.aside .section-title{position:static;width:173px;color:var(--purple)}
.first-time{position:relative;margin-top:12px;height:70px;font-size:10px;line-height:12px;color:#111}
.first-time b{font-weight:700}
.first-time p{width:110px}
.first-time .photo{position:absolute;right:8px;top:2px;width:42px;height:52px;border-radius:4px}
.mothers-day{margin-top:12px;height:40px;background:var(--purple);color:var(--white);padding:5px 8px;position:relative;border-radius:6px}
.mothers-day b{display:block;font-size:13px;font-weight:400;line-height:15px}
.mothers-day span{font-size:10px}
.mothers-day svg{position:absolute;right:10px;top:11px;width:18px;height:18px;fill:none;stroke:var(--white);stroke-width:1.6}
.info-list{list-style:none;margin-top:3px}
.info-list li{height:30px;margin-top:3px;border:1px solid var(--line);border-radius:6px;background:var(--white);display:flex;align-items:center;gap:6px;padding-left:8px;font-size:9.5px;color:#333}
.info-list li i{width:10px;height:10px;border:1px solid var(--purple);color:var(--purple);border-radius:50%;font-style:normal;font-size:9px;line-height:8px;text-align:center}
.live-help{margin-top:12px;height:40px;background:var(--orange);color:var(--white);padding:4px 10px;position:relative;border-radius:6px}
.live-help b{display:block;font-size:13px;font-weight:600;line-height:16px}
.live-help span{font-size:10.5px}
.live-help i{position:absolute;right:10px;top:6px;width:27px;height:27px;border-radius:50%;background:var(--white);color:var(--orange);font-style:normal;font-size:15px;font-weight:700;text-align:center;line-height:27px}

.site-footer{position:absolute;left:0;top:942px;width:836px;height:258px;background:var(--footer);color:var(--footer-text)}
.f-col{position:absolute;top:26px;font-size:8px;line-height:11.5px}
.f-col h5{font-size:11.5px;font-weight:400;line-height:14.5px;margin-bottom:12px;color:var(--white)}
.f-col em{font-style:normal;color:var(--footer-link)}
.pay-list{list-style:none}
.pay-list li{color:var(--footer-link);display:flex;align-items:center;gap:6px}
.pay-list svg{width:7px;height:7px;fill:none;stroke:var(--orange);stroke-width:2}
.cards{display:flex;gap:3px;margin-top:26px}
.cards span{width:30px;height:19px;background:var(--white);border-radius:3px}
.copyright{position:absolute;left:43px;top:196px;font-size:8.5px}
.footer-links{position:absolute;right:52px;top:196px;font-size:8.5px;color:var(--footer-link)}
</style>
</head>
<body>

<div class="utility-bar">
  <span class="util" style="left:347px"><svg viewBox="0 0 10 10"><circle cx="5" cy="3" r="2.5"/><path d="M0 10c0-4 10-4 10 0z"/></svg>Login <svg viewBox="0 0 10 10" style="fill:none;stroke:#fff;stroke-width:1.2"><path d="M2 3l3 3 3-3"/></svg></span>
  <span class="util" style="left:433px"><svg viewBox="0 0 10 10"><path d="M5 9L1 5a2.3 2.3 0 014-3 2.3 2.3 0 014 3z"/></svg>Wishlist (0)</span>
  <span class="util" style="left:539px"><svg viewBox="0 0 10 10"><path d="M0 1h2l1.5 5h5L10 2.5H3"/><circle cx="4" cy="8.5" r="1"/><circle cx="8" cy="8.5" r="1"/></svg>Shopping cart (0): $0.00</span>
  <span class="search-box"><svg viewBox="0 0 10 10"><circle cx="4" cy="4" r="3"/><path d="M6.3 6.3L9 9"/></svg></span>
</div>

<header class="site-header">
  <a class="brand" href="#"><span class="brand-square"></span><span class="brand-name">Parcelnook.com.au</span></a>
  <div class="perk" style="left:419px">
    <svg viewBox="0 0 20 20"><rect x="3" y="3" width="14" height="11" rx="2"/><path d="M3 9h14M6 14v3M14 14v3"/></svg>
    <div><strong>FREE SHIPPING</strong><small>on all orders over 50$</small></div>
  </div>
  <div class="perk" style="left:532px">
    <svg viewBox="0 0 20 20"><circle cx="10" cy="10" r="8"/><path d="M10 5v5h4"/></svg>
    <div><strong style="color:var(--orange)">NEXT DAY</strong><small>dispatch</small></div>
  </div>
  <div class="social"><span></span><span></span><span></span><span></span><span></span></div>
</header>

<nav class="main-nav">
  <ul>
    <li class="current">HOME</li><li>EASTER</li><li>MOTHERS DAY</li><li>GET WELL</li><li>THANK YOU</li><li>BIRTHDAY</li><li>ANNIVERSARY</li><li>ROMANCE</li><li>NEW BABY</li><li>CHILDRENS</li><li>FOR HIM</li><li>FOR HER</li>
  </ul>
</nav>

<section class="promo-banner">
  <h2>Looking for <b>Something Special?</b></h2>
  <p>Simply call customer support on: <b>+61 1300 555 018</b> FOR FURTHER INFORMATION</p>
</section>

<aside class="sidebar">
  <div class="side-block">
    <h3>Shop By Basket Price<svg class="chev" viewBox="0 0 7 5"><path d="M1 1l2.5 2.5L6 1"/></svg></h3>
    <ul><li>Gift Under $50</li><li>Gift $50 to $75</li><li>Gift $75 to $100</li><li>Gift $100 to $150</li><li>Gift Over $150</li></ul>
  </div>
  <div class="side-block">
    <h3>Shop By Basket Style<svg class="chev" viewBox="0 0 7 5"><path d="M1 1l2.5 2.5L6 1"/></svg></h3>
    <ul><li>Chocolate Bouquets</li><li>Plant Gifts</li><li>Fruit Hampers</li><li>Pamper Packs</li><li>Lollies &amp; Sweets</li><li>Teddy Bears &amp; Toys</li><li>Gourmet Hampers</li><li>Champagne &amp; Liquor</li><li>Personalised Items</li><li>Corporate Gifts</li></ul>
  </div>
  <div class="side-block">
    <h3>Shop By Occasions<svg class="chev" viewBox="0 0 7 5"><path d="M1 1l2.5 2.5L6 1"/></svg></h3>
    <ul><li>Easter Gifts</li><li>Mothers Day Gifts</li><li>Fathers Day Gifts</li><li>Christmas Gifts</li><li>Valentines Day Gifts</li></ul>
  </div>
</aside>

<a class="category" href="#" style="left:232px;--c:var(--purple-deep)">
  <div class="photo" role="img" aria-label="Teddy bear with a bottle of whisky on a wooden crate" style="background:linear-gradient(160deg,#f3ece2,#c9a46a)"></div>
  <div class="label"><b>For Him</b><span>10 Items</span></div>
</a>
<a class="category" href="#" style="left:420px;--c:var(--purple)">
  <div class="photo" role="img" aria-label="Round black gift box with red ribbon and pamper products" style="background:linear-gradient(160deg,#f4f0f0,#b8343c 70%,#333)"></div>
  <div class="label"><b>For Her</b><span>10 Items</span></div>
</a>
<a class="category" href="#" style="left:611px;--c:var(--orange)">
  <div class="photo" role="img" aria-label="Two plush toy owls in blue and purple on a wooden crate" style="background:linear-gradient(160deg,#eef6fb,#6ab8e6 55%,#9b6bd0)"></div>
  <div class="label"><b>Children</b><span>10 Items</span></div>
</a>

<h3 class="section-title" style="left:232px;top:498px;width:361px">Todays Top Products
  <span class="slider-arrows"><span><svg viewBox="0 0 5 7"><path d="M5 0v7L0 3.5z"/></svg></span><span><svg viewBox="0 0 5 7"><path d="M0 0v7l5-3.5z"/></svg></span></span>
</h3>

<div class="products">
  <article class="product featured">
    <div class="photo" role="img" aria-label="Easter gift bucket with wine, balloon and chocolate eggs" style="background:linear-gradient(160deg,#fff,#b9e08a 60%,#9b59b6)"></div>
    <h4>Vineyard Red &amp; White Double Gift</h4><div class="price">$39.00</div>
    <div class="actions"><span><i>+</i>Add to wishlist</span><span><i>+</i>Add to cart</span></div>
  </article>
  <article class="product">
    <div class="photo" role="img" aria-label="Purple gift chest with wine, cheese and crackers" style="background:linear-gradient(160deg,#fff,#7a4a9c 60%,#d9c49a)"></div>
    <h4>Chalk And Cheese Gift Chest</h4><div class="price">$89.95</div>
    <div class="actions"><span><i>+</i>Add to wishlist</span><span><i>+</i>Add to cart</span></div>
  </article>
  <article class="product">
    <div class="photo" role="img" aria-label="Basket of fresh fruit with watermelon, grapes and oranges" style="background:linear-gradient(160deg,#fff,#e0523c 50%,#7fae3a)"></div>
    <h4>Fruity Goodness</h4><div class="price">$70.00</div>
    <div class="actions"><span><i>+</i>Add to wishlist</span><span><i>+</i>Add to cart</span></div>
  </article>
  <article class="product">
    <div class="photo" role="img" aria-label="Bouquet of gold-wrapped chocolates in purple paper" style="background:linear-gradient(160deg,#fff,#c9a040 55%,#6b2a7a)"></div>
    <h4>Golden Hazelnut Bouquet</h4><div class="price">$69.00</div>
    <div class="actions"><span><i>+</i>Add to wishlist</span><span><i>+</i>Add to cart</span></div>
  </article>
  <article class="product">
    <div class="photo" role="img" aria-label="Tropical flower and fruit arrangement" style="background:linear-gradient(160deg,#fff,#e6702a 50%,#5c8a2e)"></div>
    <h4>The Tropicana</h4><div class="price">$105.00</div>
    <div class="actions"><span><i>+</i>Add to wishlist</span><span><i>+</i>Add to cart</span></div>
  </article>
  <article class="product">
    <div class="photo" role="img" aria-label="Yellow plush duck in an Easter egg gift box" style="background:linear-gradient(160deg,#fff,#f5dc6a 55%,#a8cfe8)"></div>
    <h4>Fluffy Duck Easter Egg Gift</h4><div class="price">$59.95</div>
    <div class="actions"><span><i>+</i>Add to wishlist</span><span><i>+</i>Add to cart</span></div>
  </article>
</div>

<aside class="aside">
  <h3 class="section-title">Find out more Product</h3>
  <div class="first-time">
    <p><b>First time here?</b><br>For further details about us and our current specials smply clck here</p>
    <div class="photo" role="img" aria-label="Gift box illustration with pointing hand" style="background:linear-gradient(160deg,#fdf0e0,#f7c27a 50%,#6b449b)"></div>
  </div>
  <div class="mothers-day"><b>Mother's Day</b><span>Special Gift Products</span>
    <svg viewBox="0 0 18 18"><rect x="2" y="7" width="14" height="9"/><rect x="1" y="4" width="16" height="3"/><path d="M9 4v12M9 4C7 0 4 2 6 4M9 4c2-4 5-2 3 0"/></svg>
  </div>
  <ul class="info-list">
    <li><i>+</i>Send Gifts to ...</li>
    <li><i>+</i>Searching for that Perfect Gift?</li>
    <li><i>+</i>We deliver all sorts of gifts...</li>
    <li><i>+</i>24 hours a day for Delivery...</li>
  </ul>
  <div class="live-help"><b>Live Help</b><span>Support and Services</span><i>?</i></div>
</aside>

<footer class="site-footer">
  <div class="f-col" style="left:43px;width:180px">
    <h5>Gift Baskets &amp; Hampers<br>Delivered Throughout Australia</h5>
    <p>Browse <em>Victorian</em> Delivery areas including Gifts to Melbourne Find <em>Queensland</em> Delivery locations and Gifts to Brisbane Explore <em>New South Wales</em> Delivery areas with Gifts to Sydney Discover <em>Tasmanian</em> Delivery locations including Gifts to Hobart</p>
  </div>
  <div class="f-col" style="left:257px;width:180px">
    <h5>More Australian Gift Basket<br>&amp; Hamper Delivery Locations</h5>
    <p>Find <em>South Australian</em> Delivery suburbs and Gifts to Adelaide Browse <em>ACT</em> Delivery suburbs and Gifts to Canberra Discover <em>Northern Territory</em> Delivery areas with Gifts to Darwin Explore <em>Western Australia</em> Delivery suburbs plus Gifts to Perth</p>
  </div>
  <div class="f-col" style="left:467px;width:130px">
    <h5>Payment &amp; Shipping</h5>
    <ul class="pay-list">
      <li><svg viewBox="0 0 7 7"><path d="M1 3.5l2 2L6 1"/></svg>Payment Methods</li>
      <li><svg viewBox="0 0 7 7"><path d="M1 3.5l2 2L6 1"/></svg>Shipping Guide</li>
      <li><svg viewBox="0 0 7 7"><path d="M1 3.5l2 2L6 1"/></svg>Payment Accept</li>
    </ul>
    <div class="cards"><span></span><span></span><span></span><span></span></div>
  </div>
  <div class="f-col" style="left:611px;width:180px">
    <h5>About Store</h5>
    <p><em>www.parcelnook.com.au</em> is owned by Bloomfield Trading Aus Pty Ltd, which is a 100% family owned and operated business. We have over 50 years of combined experience in business, while our parcelnook brand has delivered gift baskets and hampers since its inception in 2008.<br><br>Store Business Hours : 08:00AM - 05:00PM, AEDST</p>
  </div>
  <p class="copyright">Copyright 2014 © by <span style="color:var(--footer-link)">parcelnook.com.au</span></p>
  <p class="footer-links">Terms and Conditions | Privacy Policy | Home | About Us | Links Search Site | Contact Us</p>
</footer>

</body>
</html>
```